amber meridian consulting needs a business card

i need a business card with a logo that will also be used on the website. The company name is "Amber Meridian Consulting"
The business is an advisory and training organisation that specialises in finding a companys 'natural sequence' to success but we will also provide mentoring and counselling to individuals that want to unlock their potential. The process is unique and not full of the normal corporate bullshit so the card should be 'different' and innovative in use of texture, colour, layout etc...I have no guiding principles for you but if you were the head of a new company lloking to make a great first impression what would your card look like? It should have enough of the corporate that the stiffs dont get scared but should be cool enough that the cool kids get it :-)

Target Market(s)

Companies and people looking to grow their staff capabilities. Specialising in IT but can transcend that to other lines of business.

Industry/Entity Type

It Company

Contact Information for Business Card

usuall placeholder stuff Name, Number etc

Requirements
Must have
• cool and innovative logo and use of space
Nice to have
• Background image, subtle use of the caffeine molecule
• A rollable business card similar to the attached image. Would be nice if either side of the card could be half of a DNA helix and by rolling 2 sides together they could connect at one or more points....Perhaps the strands between have a message?
Should not have
• boring usual business card look and feel

```html
<!DOCTYPE html>
<html lang="en">
<head>
<meta charset="utf-8">
<title>Amber Meridian Consulting – Business Card</title>
<link rel="stylesheet" href="https://fonts.googleapis.com/css2?family=Saira+Semi+Condensed:wght@300;400;500&family=Barlow+Semi+Condensed:wght@500&family=Arimo:wght@400;700&display=swap">
<style>
  :root {
    --canvas-bg: #ffffff;
    --canvas-border: #a6a6a6;
    --label-grey: #6d6e71;
    --card-black: #000000;
    --card-charcoal: #1d1d1c;
    --card-olive: #10130e;
    --mint: #98c8bd;
    --mint-rule: #6f8f87;
    --slate: #6d6e71;
    --pale: #e6e6e6;
    --ink: #545454;
    --silver: #cfcfcf;
    --white: #ffffff;
  }
  * { margin: 0; padding: 0; box-sizing: border-box; }
  html, body { width: 1200px; height: 1000px; overflow: hidden; background: var(--canvas-bg); }
  .canvas {
    position: relative; width: 1200px; height: 1000px;
    border: 2px solid var(--canvas-border); background: var(--canvas-bg);
  }
  .side-label {
    position: absolute; top: 343px; width: 240px; text-align: center;
    font-family: "Barlow Semi Condensed", sans-serif; font-weight: 500;
    font-size: 42px; color: var(--label-grey); letter-spacing: 0.5px;
  }
  .side-label--front { left: 260px; }
  .side-label--back { left: 698px; }

  .card {
    position: absolute; top: 414px; width: 383px; height: 240px;
    border-radius: 13px; overflow: hidden;
  }
  .card--front {
    left: 190px;
    background: linear-gradient(90deg, var(--card-black) 0%, var(--card-black) 12%, #0d0d0d 40%, var(--card-charcoal) 70%, #1a1a18 85%, var(--card-olive) 100%);
  }
  .front-wordmark {
    position: absolute; left: 0; right: 0; top: 60px; text-align: center;
    font-family: "Saira Semi Condensed", sans-serif; font-weight: 300;
    font-size: 62px; line-height: 1; color: var(--mint); letter-spacing: 3px;
  }
  .front-company {
    position: absolute; left: 0; right: 0; top: 146px; text-align: center;
    font-family: "Saira Semi Condensed", sans-serif; font-weight: 400;
    font-size: 20px; color: var(--silver); letter-spacing: 0.3px;
  }

  .card--back { left: 627px; background: var(--mint); }
  .back-swoosh { position: absolute; inset: 0; }
  .rule { position: absolute; height: 1px; background: var(--mint-rule); }
  .rule--top { left: 53px; top: 29px; width: 187px; }
  .rule--bottom { left: 53px; top: 162px; width: 180px; }
  .holder-name {
    position: absolute; left: 56px; top: 37px;
    font-family: "Arimo", sans-serif; font-weight: 700; font-size: 19px; color: var(--ink);
  }
  .holder-title {
    position: absolute; left: 57px; top: 62px;
    font-family: "Arimo", sans-serif; font-weight: 700; font-size: 9.5px;
    letter-spacing: 1px; color: var(--ink);
  }
  .contact-list {
    position: absolute; left: 56px; top: 100px; list-style: none;
    font-family: "Arimo", sans-serif; font-weight: 700; font-size: 9.5px;
    letter-spacing: 0.6px; color: var(--ink); line-height: 16px;
  }
  .contact-list li:nth-child(4) { line-height: 13px; }
  .contact-web {
    position: absolute; left: 56px; top: 165px;
    font-family: "Arimo", sans-serif; font-weight: 700; font-size: 9.5px;
    letter-spacing: 0.8px; color: var(--ink);
  }
  .back-wordmark {
    position: absolute; right: 26px; top: 179px;
    font-family: "Saira Semi Condensed", sans-serif; font-weight: 300;
    font-size: 34px; line-height: 1; color: var(--white); letter-spacing: 1px;
  }
</style>
</head>
<body>
<main class="canvas">
  <h2 class="side-label side-label--front">FRONT</h2>
  <h2 class="side-label side-label--back">BACK</h2>

  <section class="card card--front" aria-label="Card front">
    <p class="front-wordmark">AMC</p>
    <p class="front-company">Amber Meridian Consulting</p>
  </section>

  <section class="card card--back" aria-label="Card back">
    <svg class="back-swoosh" width="383" height="240" viewBox="0 0 383 240" aria-hidden="true">
      <path d="M14,240 Q255,205 383,55 L383,240 Z" fill="var(--pale)"/>
      <path d="M18,240 Q280,222 383,83 L383,240 Z" fill="var(--slate)"/>
    </svg>
    <span class="rule rule--top"></span>
    <p class="holder-name">YOUR NAME</p>
    <p class="holder-title">DIRECTOR</p>
    <ul class="contact-list">
      <li>555-014-2290</li>
      <li>Harbor Vale FL 30417</li>
      <li>PO Box 118204</li>
      <li>mhale@ambermail.com</li>
    </ul>
    <span class="rule rule--bottom"></span>
    <p class="contact-web">www.ambermeridian.com</p>
    <p class="back-wordmark">AMC</p>
  </section>
</main>
</body>
</html>
```